Q-Rolls Business Card

We are a modern retail clothing store. Established in 1994. I need a presentable card that will amaze vendors when given to them.

Front: Logo in middle
Info Side:

Name: Tomas Velder
Cell: 630-812-4463
Work: 630-917-3384 EXT. 417
Email: Tomas@q-rolls-example.com
Website: www.Q-rolls-example.com

Industry/Entity Type

Business

```html
<!DOCTYPE html>
<html lang="en">
<head>
<meta charset="utf-8">
<title>Q-Rolls Business Card</title>
<link href="https://fonts.googleapis.com/css2?family=Lato:wght@400;700&display=swap" rel="stylesheet">
<style>
  :root {
    --backdrop: #e6e7e9;
    --ink: #151515;
    --paper: #ffffff;
    --night: #0b0b0b;
    --muted: #2b2b2b;
    --rule: #bdbdbd;
  }
  * { margin: 0; padding: 0; box-sizing: border-box; }
  html, body { width: 1200px; height: 898px; overflow: hidden; }
  body {
    background: var(--backdrop);
    font-family: "Lato", Arial, sans-serif;
    position: relative;
  }
  .card {
    position: absolute;
    left: 280px;
    width: 640px;
    height: 366px;
    box-shadow: 0 6px 14px rgba(0,0,0,0.18);
  }
  .card--front {
    top: 58px;
    background: var(--night);
    color: var(--paper);
  }
  .card--back {
    top: 474px;
    background: var(--paper);
    color: var(--ink);
  }
  .brand {
    font-weight: 700;
    text-transform: uppercase;
    letter-spacing: 0.04em;
    line-height: 1;
    white-space: nowrap;
  }
  .card--front .brand {
    position: absolute;
    left: 0; right: 0;
    top: 128px;
    text-align: center;
    font-size: 92px;
  }
  .card--front .web {
    position: absolute;
    left: 0; right: 0;
    bottom: 40px;
    text-align: center;
    font-size: 15px;
    letter-spacing: 0.16em;
  }
  .card--back .brand-area {
    position: absolute;
    left: 0; top: 0;
    width: 318px; height: 100%;
    display: flex;
    align-items: center;
    justify-content: center;
  }
  .card--back .brand { font-size: 52px; }
  .divider {
    position: absolute;
    left: 318px;
    top: 30px;
    width: 2px;
    height: 306px;
    background: linear-gradient(to bottom, rgba(0,0,0,0) 0%, var(--rule) 30%, var(--rule) 70%, rgba(0,0,0,0) 100%);
  }
  .contact {
    position: absolute;
    left: 356px;
    top: 122px;
    list-style: none;
  }
  .contact .name {
    font-size: 26px;
    font-weight: 400;
    margin-bottom: 8px;
    color: var(--muted);
  }
  .contact li {
    display: flex;
    align-items: center;
    gap: 12px;
    font-size: 17px;
    line-height: 25px;
    color: var(--muted);
  }
  .contact svg { width: 14px; height: 14px; flex: none; fill: var(--ink); }
</style>
</head>
<body>
  <section class="card card--front" aria-label="Card front">
    <div class="brand">Q-Rolls</div>
    <div class="web">www.Q-rolls-example.com</div>
  </section>

  <section class="card card--back" aria-label="Card back">
    <div class="brand-area"><div class="brand">Q-Rolls</div></div>
    <div class="divider"></div>
    <div class="contact">
      <div class="name">Tomas Velder</div>
      <ul>
        <li>
          <svg viewBox="0 0 16 16" aria-hidden="true"><path d="M3.5 1l2.5 3-1.5 1.8c.9 2 2.4 3.5 4.4 4.4L10.7 8.7l3.3 2.5-1.6 2.9C7 13.6 2.4 9 1.8 3.2z"/></svg>
          630-812-4463
        </li>
        <li>
          <svg viewBox="0 0 16 16" aria-hidden="true"><path d="M4 0h8a1 1 0 0 1 1 1v14a1 1 0 0 1-1 1H4a1 1 0 0 1-1-1V1a1 1 0 0 1 1-1zm1 2v9h6V2zm3 10.5a1 1 0 1 0 0 2 1 1 0 0 0 0-2z"/></svg>
          630-917-3384 EXT. 417
        </li>
        <li>
          <svg viewBox="0 0 16 16" aria-hidden="true"><path d="M1 3h14v10H1zm1.5 1.2v.3L8 8.6l5.5-4.1v-.3zM2.5 6.2v5.3h11V6.2L8 10.3z"/></svg>
          Tomas@q-rolls-example.com
        </li>
        <li>
          <svg viewBox="0 0 16 16" aria-hidden="true"><path d="M8 1a7 7 0 1 0 0 14A7 7 0 0 0 8 1zm5.4 6.2h-2.3a11 11 0 0 0-.8-3.9 5.5 5.5 0 0 1 3.1 3.9zM8 2.6c.7.9 1.4 2.5 1.6 4.6H6.4C6.6 5.1 7.3 3.5 8 2.6zM5.7 3.3a11 11 0 0 0-.8 3.9H2.6a5.5 5.5 0 0 1 3.1-3.9zM2.6 8.8h2.3c.1 1.5.4 2.8.8 3.9a5.5 5.5 0 0 1-3.1-3.9zM8 13.4c-.7-.9-1.4-2.5-1.6-4.6h3.2c-.2 2.1-.9 3.7-1.6 4.6zm2.3-.7c.4-1.1.7-2.4.8-3.9h2.3a5.5 5.5 0 0 1-3.1 3.9z"/></svg>
          www.Q-rolls-example.com
        </li>
      </ul>
    </div>
  </section>
</body>
</html>
```